Lawn Maintenance Company needs attractive add for local newspaper

My company Fennick Yard Service offers many lawn and yard services but I want this add to focus on one specific service we offer.
- Lawn Fertilizer and Weed Control -

This will be an add for our local newspaper, likely a 1/4 page

Some more information about this service.
Our customers generally call us when their lawn is over run with weeds or is performing poorly. Most of the time we set them up with a program and we return to their property every 4 - 5 weeks for another application. 95% of our customers return the following year for the same program. If the customer wishes we will also do a one time application

email: fennickyardservice@example.net
phone: call or text 555-418-7390

Target Market(s)

- Local small towns, populations less than 20,000
- Residential and Commercial customers with lawns
- People who are using the competitors service and aren't happy with it

Industry/Entity Type

Lawn Care

Requirements
Must have
• Must include our logo, email address and phone number
• - Logo
• - Email address and phone number (call or text)
• - Must focus on the service we want to sell (fertilizer and weed control)
Nice to have
• Some phrases or words that should be included, does not need to be word for word as long as the point is made
• - We service both Residential & Commercial properties
• - We offer professional service that can dramatically improve your lawn whether you are looking for a single application or a season long fertilizer/weed control program
• - Our lawn techs are licensed and certified applicators
Should not have
• I do not want any stock pictures of people, houses or equipment.

```html
<!DOCTYPE html>
<html lang="en">
<head>
<meta charset="utf-8">
<title>Fennick Yard Service – Lawn Fertilizer and Weed Control</title>
<link rel="stylesheet" href="https://fonts.googleapis.com/css2?family=Carlito:wght@400;700&display=swap">
<style>
  :root {
    --page: #ffffff;
    --leaf-light: #b8dc3c;
    --leaf-mid: #7fbf1e;
    --leaf-deep: #4f8f16;
    --panel: #ffffff;
    --ink: #3a3a3a;
    --brand: #1f5a32;
  }
  * { margin: 0; padding: 0; box-sizing: border-box; }
  html, body {
    width: 1200px;
    height: 1200px;
    overflow: hidden;
    background: var(--page);
  }
  .ad {
    position: relative;
    width: 1200px;
    height: 1200px;
    font-family: "Carlito", "Calibri", Arial, sans-serif;
    color: var(--ink);
    font-weight: 700;
  }
  .leaf-frame {
    position: absolute;
    left: 29px;
    top: 26px;
    width: 1133px;
    height: 1132px;
    background:
      radial-gradient(ellipse at 15% 10%, var(--leaf-light), transparent 45%),
      radial-gradient(ellipse at 85% 90%, var(--leaf-light), transparent 45%),
      linear-gradient(135deg, var(--leaf-mid), var(--leaf-deep) 50%, var(--leaf-mid));
  }
  .panel {
    position: absolute;
    left: 55px;
    top: 49px;
    width: 1083px;
    height: 1086px;
    background: var(--panel);
  }
  .brand-name {
    position: absolute;
    left: 332px;
    top: 80px;
    width: 484px;
    height: 304px;
    display: flex;
    align-items: center;
    justify-content: center;
    text-align: center;
    font-size: 64px;
    line-height: 1.05;
    font-weight: 700;
    color: var(--brand);
  }
  .pitch {
    position: absolute;
    left: 101px;
    top: 404px;
    font-size: 26.5px;
    line-height: 38.3px;
  }
  .pitch span { display: block; white-space: nowrap; }
  .contact {
    position: absolute;
    left: 0;
    top: 748px;
    width: 1200px;
  }
  .contact-heading {
    text-align: center;
    font-size: 19px;
    text-decoration: underline;
    padding-left: 0;
    margin-left: -26px;
  }
  .contact-line {
    margin-left: 385px;
    font-size: 22.5px;
    line-height: 31px;
    text-decoration: underline;
  }
  .contact-heading + .contact-line { margin-top: 8px; }
  .highlights {
    position: absolute;
    left: 176px;
    top: 862px;
    list-style: none;
    font-size: 21.5px;
    line-height: 31.3px;
  }
  .highlights li { text-decoration: underline; white-space: nowrap; }
</style>
</head>
<body>
  <main class="ad">
    <div class="leaf-frame" role="img" aria-label="Frame of fresh green grass blades"></div>
    <div class="panel"></div>

    <div class="brand-name">Fennick<br>Yard Service</div>

    <p class="pitch">
      <span>My company Fennick Yard Service offers many lawn services which my regular</span>
      <span>and new customers are now familiar and are happy with, I would like to extend</span>
      <span>&nbsp;this service to all. “Lawn Fertilizer and Weed Control”, will be widely advertised.</span>
      <span>Our usual method of lawn care was one where a customer would call us when</span>
      <span>their lawn is over run with weeds, or is performing poorly.</span>
      <span>Most of the time we set them up with a program and we return to their property</span>
      <span>every 4 - 5 weeks for another application. 95% of our customers return the</span>
      <span>following year for the same program. If the customer wishes we will also do a</span>
      <span>one time application.</span>
    </p>

    <section class="contact">
      <h2 class="contact-heading">Contact Details</h2>
      <p class="contact-line">email: fennickyardservice@example.net</p>
      <p class="contact-line">phone: call or text 555-418-7390</p>
    </section>

    <ul class="highlights">
      <li>- - We service both Residential &amp; Commercial properties</li>
      <li>- - We offer single applications or season long fertilizer/weed control programs</li>
      <li>- - All of our technicians are certified by Alberta Environment</li>
    </ul>
  </main>
</body>
</html>
```